Flyer needed to promote gutter clearance service for established gardening company

We need a bright and engaging flyer to be designed to advertise our gutter clearance service.
Whilst we are a gardening company that normally does more horticultural work, during the winter we offer other services such as gutter clearance where we remove the debris from gutters and thereby reducing the risk of clogs, leakage, breakage and potential structural damage to the property.

Full details of our service, together with our overall brand and colours can be seen on www.marlowtreecare.co.uk/gutters.

We would like you to use the page on the website as a basis to create the flyer and so please feel free to use as much or as little of the wording contained within the webpage on the flyer drawing particular attention to "Prices starting at just £60 for an average 3 bed house". I will upload pictures but please feel free to use other graphics and fonts to make it stand out.

The contact details which should be included within the flyer are as follows:

Marlow Treecare Services Ltd
Orbit Trading Centre
Fairbrook Vale Ind Estate
Swindon
SN4 7HW

Tel: 01793 418302
www.marlowtreecare.co.uk
dean@marlowtreecare.co.uk

The flyers will eventually be printed out in A5 (210mm x 148mm) using Printelle and so needs to be in that size and suitable file for upload.

I have only put this as a 2 day project as its really urgent and I'm hoping we get some great designs in that time.

Target Market(s)

Homeowners between 25 - 65+

Industry/Entity Type

Home Improvement

Font styles to use
Serif
Sans Serif
Decorative
Script

Colors
6b449b
9bcb3c

Requirements
Must have
• Our colours are purple and green as seen on our website www.marlowtreecare.co.uk/gutters. Please use those colours.
• The flyer should draw attention to the following facts:
• We are Marlow Treecare Services Ltd (see attached logo)
• We are offering a Gutter Clearance Service in Swindon
• Prices start at just £60 for the average 3 bed house.
• We are fully insured.
• Our contact details must be included (as in the product description above)
• I have attached pictures but feel free to add other graphics or use fonts to make the flyer more engaging and interesting.
• Additional wording may be taken from the website at the address shown above. You can use as much or as little wording as you like just as long as the message gets across and the flyer contains our contact information and logo and the details shown above.
Nice to have
• I would like a bright and modern design which isn't too busy or cluttered. It should be something that is quick and easy to read.
Should not have
• I don't want it to look too busy or crowded with small type which people just won't read. Whilst I've said you can take whatever wording you want from our website, I'd suggest you don't take it all or too much. I want the main message (as detailed above in 'must haves') to stand out rather than have it contained deep within lots of small type face.

```html
<!DOCTYPE html>
<html lang="en">
<head>
<meta charset="utf-8">
<title>Marlow Treecare – Gutter Clearance Flyer</title>
<link href="https://fonts.googleapis.com/css2?family=Oswald:wght@400;500;600&display=swap" rel="stylesheet">
<style>
  :root {
    --purple: #6b449b;
    --green: #9bcb3c;
    --lime: #c6d450;
    --olive: #a9bd3e;
    --mint: #d8eec4;
    --peach: #f2d6b3;
    --paper: #ffffff;
    --ink: #3a2c22;
    --stage: #d9d9d9;
  }
  * { box-sizing: border-box; margin: 0; padding: 0; }
  html, body {
    width: 1200px; height: 700px; overflow: hidden;
    background: var(--stage);
    font-family: "Oswald", "Arial Narrow", sans-serif;
  }
  .flyer {
    position: absolute; left: 365px; top: 18px;
    width: 470px; height: 664px;
    background: var(--paper);
    overflow: hidden;
    box-shadow: 0 6px 18px rgba(0,0,0,.18);
  }
  .hero { position: absolute; left: 0; top: 0; width: 470px; height: 250px; background: var(--mint); }
  .photo { position: absolute; }
  .photo-blower {
    left: 0; top: 0; width: 250px; height: 96px;
    clip-path: polygon(0 0, 100% 0, 88% 100%, 0 100%);
    background: linear-gradient(120deg, #7a8f5a 0%, #c0512e 35%, #2b2b2b 60%, #d8834a 85%, #9aa6a0 100%);
  }
  .photo-gloves {
    left: 262px; top: 0; width: 208px; height: 250px;
    clip-path: polygon(10% 0, 100% 0, 100% 100%, 0 100%);
    background: linear-gradient(160deg, #2e3236 0%, #5f8a3a 35%, #d99a3c 55%, #3d8d80 75%, #6d7e3e 100%);
  }
  .intro {
    position: absolute; left: 18px; top: 84px; width: 300px; height: 150px;
    background: linear-gradient(135deg, var(--lime), var(--olive));
    clip-path: polygon(0 0, 100% 8%, 100% 100%, 0 100%);
    padding: 26px 18px 12px 20px;
    color: var(--ink);
    font-size: 10.5px; font-weight: 500; line-height: 1.4;
    text-transform: uppercase; letter-spacing: .6px;
  }
  .price-band {
    position: absolute; left: 0; top: 250px; width: 470px; height: 62px;
    background: var(--purple);
    color: #fff; font-size: 19px; font-weight: 500; line-height: 1.2;
    padding: 8px 22px; text-align: center;
  }
  .accent-band { position: absolute; left: 0; top: 312px; width: 470px; height: 14px; background: var(--peach); }
  .label {
    position: absolute; font-size: 17px; font-weight: 600;
    letter-spacing: 7px; text-transform: uppercase;
  }
  .label-before { left: 18px; top: 326px; color: var(--green); }
  .label-after { right: 12px; top: 458px; color: var(--purple); }
  .photo-before {
    left: 0; top: 354px; width: 470px; height: 102px;
    background: linear-gradient(100deg, #6e6a5c 0%, #b49a62 30%, #8b7a4e 55%, #c9c3b2 70%, #7fa845 100%);
  }
  .photo-after {
    left: 0; top: 486px; width: 470px; height: 68px;
    background: linear-gradient(100deg, #8a7e74 0%, #b8b2a8 40%, #dcdad6 60%, #6fa23c 100%);
  }
  .footer {
    position: absolute; left: 0; top: 554px; width: 470px; height: 110px;
    padding: 12px 20px; color: var(--ink);
    font-size: 10px; line-height: 1.35; text-transform: uppercase; letter-spacing: .6px;
  }
  .address { position: absolute; left: 20px; top: 12px; }
  .contact { position: absolute; left: 220px; top: 12px; }
  .brand {
    position: absolute; right: 20px; bottom: 14px;
    display: flex; align-items: center; gap: 8px;
  }
  .brand-mark { width: 22px; height: 22px; border-radius: 50%; background: var(--green); }
  .brand-name { font-size: 20px; font-weight: 500; color: var(--ink); letter-spacing: .5px; }
</style>
</head>
<body>
  <main class="flyer">
    <section class="hero">
      <div class="photo photo-blower" role="img" aria-label="Photo of a gardener clearing autumn leaves with a leaf blower"></div>
      <div class="photo photo-gloves" role="img" aria-label="Photo of gloved hands lifting leaves out of a gutter"></div>
      <p class="intro">Clearing gutters is not just a dirty job but it can be a dangerous one too if not done properly. At Marlow Treecare Services we are fully insured and use the latest tools and techniques to safely clear your gutters, giving you peace of mind without having to risk getting dirty or injured yourself.</p>
    </section>

    <h1 class="price-band">with prices starting at just £60 to clear the gutters of an average 3 bed house!</h1>
    <div class="accent-band"></div>

    <span class="label label-before">Before</span>
    <div class="photo photo-before" role="img" aria-label="Photo of a gutter clogged with leaves and debris"></div>
    <span class="label label-after">After</span>
    <div class="photo photo-after" role="img" aria-label="Photo of the same gutter cleared and clean"></div>

    <footer class="footer">
      <address class="address" style="font-style:normal">
        Marlow Treecare Services Ltd<br>
        Orbit Trading Centre<br>
        Fairbrook Vale Ind Estate<br>
        Swindon<br>
        SN4 7HW
      </address>
      <div class="contact">
        Tel: 01793 418302<br>
        www.marlowtreecare.co.uk<br>
        dean@marlowtreecare.co.uk
      </div>
      <div class="brand">
        <span class="brand-mark"></span>
        <span class="brand-name">Marlow Treecare Services</span>
      </div>
    </footer>
  </main>
</body>
</html>
```